Larkspur Ridge Management - Business Cards

I need business cards. My current logo was designed by a designer at this site and I very much like and am happy with the results. I would like a business card that is trendy, unique, current yet professional. I deal with high net worth clients daily

Target Market(s)

Out of state investors looking to get into the rental market in Ohio

Industry/Entity Type

Property Management, Consulting

Contact Information for Business Card

Name, Title (Chief Financial Officer) office phone number (555) 817-3094 website address larkridgemgmt.example

Font styles to use
Sans Serif

Colors
0054AA
0677BA
7BADD7
CADEEF
E8F1F8
0094D4
00A9DD
6FCCEA
C7EBF8
E9F6FB
00AB8E
00BBA5
67D7C9
C6EFE9
E9F9F6

```html
<!DOCTYPE html>
<html lang="en">
<head>
<meta charset="utf-8">
<title>Larkspur Ridge Management – Business Cards</title>
<link rel="stylesheet" href="https://fonts.googleapis.com/css2?family=Open+Sans:wght@400;600;700&display=swap">
<style>
  :root {
    --backdrop: #c8c8c8;
    --navy: #243356;
    --red: #d0232e;
    --white: #ffffff;
    --grey-text: #555a60;
  }
  * { margin: 0; padding: 0; box-sizing: border-box; }
  html, body {
    width: 1107px;
    height: 1200px;
    overflow: hidden;
    background: var(--backdrop);
    font-family: "Open Sans", Arial, sans-serif;
  }
  .canvas { position: relative; width: 1107px; height: 1200px; }
  .card {
    position: absolute;
    left: 141px;
    width: 825px;
    height: 471px;
    border-radius: 22px;
    overflow: hidden;
  }
  .card--front { top: 98px; background: var(--white); }
  .card--back { top: 630px; background: var(--navy); }

  .front-band {
    position: absolute;
    left: 0; right: 0;
    top: 332px; bottom: 0;
    background: var(--navy);
    border-top: 7px solid var(--red);
  }
  .holder { position: absolute; left: 40px; top: 56px; }
  .holder__name {
    color: var(--red);
    font-weight: 700;
    font-size: 29px;
    line-height: 1.1;
    letter-spacing: 0.3px;
  }
  .holder__title {
    color: var(--grey-text);
    font-size: 23px;
    line-height: 1.3;
  }
  .contact {
    position: absolute;
    left: 40px; top: 364px;
    list-style: none;
    color: var(--white);
    font-size: 23px;
    line-height: 30px;
  }
  .contact__item { display: flex; align-items: center; gap: 7px; }
  .contact__icon { width: 17px; height: 17px; flex: none; }

  .brand-name {
    position: absolute;
    text-align: center;
    font-weight: 700;
    line-height: 1.15;
    text-transform: uppercase;
  }
  .card--front .brand-name {
    left: 420px; width: 370px; top: 150px;
    color: var(--navy);
    font-size: 34px;
  }
  .card--back .brand-name {
    left: 0; width: 825px; top: 170px;
    color: var(--white);
    font-size: 38px;
  }
</style>
</head>
<body>
<main class="canvas">
  <section class="card card--front" aria-label="Business card front">
    <div class="front-band"></div>
    <div class="holder">
      <h1 class="holder__name">DANIEL WHITMORE</h1>
      <p class="holder__title">Chief Financial Officer</p>
    </div>
    <ul class="contact">
      <li class="contact__item">
        <svg class="contact__icon" viewBox="0 0 20 20" aria-hidden="true">
          <path fill="#d0232e" d="M2 7c0-3 4-4 8-4s8 1 8 4l-3 1-1-2c-2-1-6-1-8 0L5 8zM5 9l2-2h6l2 2 1 7H4z"/>
          <circle cx="10" cy="12" r="2" fill="#243356"/>
        </svg>
        (555) 817-3094
      </li>
      <li class="contact__item">
        <svg class="contact__icon" viewBox="0 0 20 20" aria-hidden="true">
          <circle cx="10" cy="10" r="9" fill="#d0232e"/>
          <path fill="#243356" d="M6 5c2 0 3 2 2 3s-3 1-2 3 1 3 0 4C3 13 3 7 6 5zm7 3c2 0 3 2 2 4s-2 2-3 1 0-2-1-3 0-2 2-2z"/>
        </svg>
        www.larkridgemgmt.example
      </li>
    </ul>
    <p class="brand-name">Larkspur<br>Ridge<br>Management</p>
  </section>

  <section class="card card--back" aria-label="Business card back">
    <p class="brand-name">Larkspur<br>Ridge<br>Management</p>
  </section>
</main>
</body>
</html>
```